I am medical doctor in surgery specialized in Urology and anti-aging. I need Web and Instagram design for a head cream , face cream and body lotion. I did a 2% GHK-Cu solution (head-face-body) with an professional pharmacist specialized in manufacturing creams. . GHK-Cu is a tri-peptide with solid scientific background to rejuvenate the skin (will stimulate collagen production) and can promote hair regrowth. Statistically 70% of peptides bought are fake on the market, I can personally guarantee about purity (my peptides are certified pure above 99% checked in an independent laboratory in London -UK.
I want to use the name 'Lunavel'. I secured already the domain names. I had an design for another project I could re-use for this project. The ribbon should include more blue. The font of Lunavel can be changed. I got a logo which is ok for me. Web design best coded with Wordpress.

Target Market(s)

Anti aging, skin care, hair regrowth, skin collagen

Industry/Entity Type

the cream can also be used after surgery for faster and better wound healing

Number of Pages Required

5+ page

Font styles to use
Sans Serif

Colors
0054AA
0677BA
7BADD7
CADEEF
E8F1F8

Requirements
Must have
• target population 30-70 years
Nice to have
• scientific proof, pictures before-after
Should not have
• GHK-Cu has solid scientific animal studies of anti-cancer properties. It is 100% safe for dermal human use.

```html
<!DOCTYPE html>
<html lang="en">
<head>
<meta charset="utf-8">
<title>Lunavel — Clinically Proven Skin Renewal</title>
<link href="https://fonts.googleapis.com/css2?family=Inter:wght@400;500;600;700&family=Manrope:wght@500;600;700&display=swap" rel="stylesheet">
<style>
:root{
  --blue:#1f55b0;
  --blue-deep:#0054AA;
  --blue-mid:#0677BA;
  --blue-soft:#7BADD7;
  --blue-pale:#CADEEF;
  --blue-mist:#E8F1F8;
  --navy:#1b2140;
  --ink:#1a1a1a;
  --muted:#777;
  --grey-band:#f3f3f3;
  --gold:#f2b01e;
  --white:#fff;
}
*{margin:0;padding:0;box-sizing:border-box}
html,body{width:1200px;height:3480px;overflow:hidden}
body{font-family:"Inter",sans-serif;color:var(--ink);background:var(--white);position:relative}
h1,h2,h3{font-family:"Manrope",sans-serif}
.wrap{position:absolute;left:125px;right:125px}
.section{position:absolute;left:0;width:1200px}

/* header */
.site-header{top:0;height:100px}
.brand{position:absolute;left:125px;top:34px;display:flex;align-items:center;gap:10px;font-weight:700;font-size:24px;color:var(--blue-deep)}
.brand-dot{width:24px;height:24px;border-radius:50%;background:var(--blue-mid)}
.main-nav{position:absolute;left:344px;top:45px;display:flex;gap:30px;font-size:14px;color:#333}
.ship-note{position:absolute;left:844px;top:49px;font-size:10px;color:#999;letter-spacing:.3px}
.btn-header{position:absolute;left:956px;top:30px;width:119px;height:48px;background:var(--blue-deep);color:#fff;font-size:13px;font-weight:600;display:flex;align-items:center;justify-content:center}

/* hero */
.hero{top:100px;height:708px}
.hero-panel{position:absolute;left:0;top:0;width:600px;height:708px;background:var(--blue)}
.eyebrow{display:flex;align-items:center;gap:20px;font-size:10px;letter-spacing:.3px}
.eyebrow::before{content:"";width:52px;height:1px;background:currentColor}
.hero .eyebrow{position:absolute;left:125px;top:42px;color:#fff}
.hero h1{position:absolute;left:125px;top:76px;color:#fff;font-size:62px;line-height:77px;font-weight:700;letter-spacing:-.5px}
.hero-lead{position:absolute;left:125px;top:314px;width:405px;color:#fff;font-size:11.5px;line-height:23px}
.hero-points{position:absolute;left:125px;top:443px;list-style:none;color:#fff;font-size:13px;font-weight:600}
.hero-points li{height:29px;display:flex;align-items:center;gap:11px}
.hero-points li::before{content:"";width:10px;height:10px;border-radius:50%;background:#fff}
.btn-light{position:absolute;background:#fff;color:var(--ink);font-size:13.5px;font-weight:600;display:flex;align-items:center;justify-content:center;gap:6px}
.hero .btn-light{left:125px;top:595px;width:216px;height:68px}
.hero-visual{position:absolute;left:600px;top:0;width:600px;height:708px;background:
  radial-gradient(ellipse 45% 40% at 30% 45%,rgba(236,205,186,.9),transparent 70%),
  radial-gradient(ellipse 45% 40% at 75% 45%,rgba(226,190,168,.9),transparent 70%),
  linear-gradient(180deg,#d9c3ae 0%,#c9a488 45%,#a98068 100%)}
.hero-divider{position:absolute;left:317px;top:0;width:3px;height:708px;background:#fff}
.hero-tag{position:absolute;top:630px;color:#fff;text-align:center}
.hero-tag strong{display:block;font-family:"Manrope",sans-serif;font-size:25px;font-weight:700}
.hero-tag span{font-size:13px}

/* features */
.features{top:808px;height:188px;background:var(--grey-band)}
.feature{position:absolute;top:32px;width:220px}
.feature h3{font-size:16.5px;font-weight:700;margin-bottom:14px}
.feature p{font-size:10.2px;line-height:19.5px;color:#777}
.feature + .feature::before{content:"";position:absolute;left:-20px;top:0;width:1px;height:128px;background:#ddd}

/* section heads */
.sec-head .eyebrow{color:var(--ink);margin-bottom:20px}
.sec-head h2{font-size:26px;font-weight:700;margin-bottom:18px}
.sec-head p{font-size:11.5px;color:#888}

/* gallery */
.gallery{top:996px;height:480px}
.gallery .sec-head{top:66px}
.view-all{position:absolute;right:125px;top:140px;font-size:12px;color:var(--blue-deep)}
.case{position:absolute;top:190px;width:310px;height:232px}
.case-photo{position:absolute;top:0;width:155px;height:200px}
.case-photo span{position:absolute;left:9px;bottom:18px;color:#fff;font-size:11px;font-weight:600}
.case-bar{position:absolute;left:0;bottom:0;width:310px;height:32px;background:#1b4c8c;color:#fff;display:flex;align-items:center;justify-content:space-between;padding:0 9px;font-size:10px;font-weight:600}
.case-bar small{font-size:9px;font-weight:500}

/* products */
.products{top:1476px;height:684px;background:var(--blue-mist)}
.products .sec-head{top:52px}
.product{position:absolute;top:173px;width:310px;height:461px;background:#fff}
.product-shot{position:absolute;left:90px;top:35px;width:130px;height:190px;border-radius:14px 14px 8px 8px}
.product-tag{position:absolute;left:27px;top:252px;font-size:15px}
.product h3{position:absolute;left:27px;top:284px;font-size:18.5px;font-weight:700}
.product p{position:absolute;left:27px;top:312px;width:240px;font-size:11px;line-height:16px;color:#888}
.stars{color:var(--gold);font-size:11px;letter-spacing:1px}
.product .stars{position:absolute;left:27px;top:374px}
.price{position:absolute;left:27px;top:396px;font-size:19px;font-weight:600}

/* doctor */
.doctor{top:2160px;height:408px}
.doctor-visual{position:absolute;left:0;top:0;width:600px;height:408px;background:
  radial-gradient(ellipse 30% 45% at 50% 70%,rgba(240,242,246,.85),transparent 70%),
  linear-gradient(180deg,#d6dde5 0%,#aebfd1 45%,#4d7ab3 100%)}
.doctor-copy{position:absolute;left:642px;top:38px;width:425px}
.doctor-copy .eyebrow{margin-bottom:24px}
.doctor-copy h2{font-size:25px;line-height:30px;font-weight:700;margin-bottom:18px}
.doctor-copy p{font-size:11px;line-height:21px;color:#777}
.doctor-quote{margin-top:26px;border-left:3px solid var(--blue-deep);padding-left:18px;font-size:11px;line-height:21px;font-style:italic;color:#222}

/* testimonials */
.reviews{top:2568px;height:499px}
.reviews .sec-head{top:55px}
.review{position:absolute;top:172px;width:301px;height:251px;background:#fff;border-radius:6px;box-shadow:0 2px 16px rgba(0,0,0,.06);padding:27px 27px}
.review p{margin-top:18px;font-size:11px;line-height:20px;color:#555}
.reviewer{position:absolute;left:27px;top:165px;display:flex;align-items:center;gap:17px}
.avatar{width:60px;height:60px;border-radius:50%;background:linear-gradient(135deg,#8a7566,#3a3230)}
.reviewer strong{display:block;font-size:16px;font-weight:500;margin-bottom:8px}
.reviewer span{font-size:12px;color:#999}

/* cta */
.cta{top:3067px;height:229px;background:
  radial-gradient(ellipse 40% 60% at 20% 100%,rgba(90,130,190,.35),transparent 70%),
  linear-gradient(90deg,#1d3f7d,#25508f 60%,#1c3b77)}
.cta h2{position:absolute;left:125px;top:62px;color:#fff;font-size:28px;font-weight:700}
.cta p{position:absolute;left:125px;top:116px;width:510px;color:#fff;font-size:11.5px;line-height:21px}
.cta .btn-light{left:866px;top:64px;width:209px;height:70px;font-size:14px}
.cta-link{position:absolute;right:125px;top:158px;color:#fff;font-size:14px;font-weight:500}

/* footer */
.site-footer{top:3296px;height:184px;background:var(--navy);color:#8a93c0}
.foot-brand{position:absolute;left:65px;top:48px;color:#fff;font-size:18px;font-weight:600;letter-spacing:2px}
.foot-tag{position:absolute;left:65px;top:82px;width:280px;font-size:10px;line-height:18px}
.foot-copy{position:absolute;left:65px;top:134px;font-size:8.5px}
.foot-col{position:absolute;top:45px;list-style:none;font-size:10px;line-height:22px}
.foot-col li:first-child{font-size:8.5px;font-weight:700;letter-spacing:1px;color:var(--blue-soft);margin-bottom:2px}
</style>
</head>
<body>

<header class="section site-header">
  <div class="brand"><span class="brand-dot"></span>Lunavel</div>
  <nav class="main-nav"><span>Science</span><span>Products</span><span>Before &amp; After</span><span>About</span><span>Journal</span></nav>
  <span class="ship-note">FREE SHIPPING EU</span>
  <a class="btn-header">Shop Now</a>
</header>

<section class="section hero">
  <div class="hero-panel"></div>
  <div class="eyebrow">MEDICAL GRADE • GHK-CU PEPTIDE COMPLEX</div>
  <h1>Clinically<br>Proven<br>Skin Renewal</h1>
  <p class="hero-lead">The only 2% GHK-Cu formulation personally guaranteed by a medical doctor.<br>Laboratory certified for 99%+ purity, independently verified in the UK to deliver exceptional skin rejuvenation, collagen support, and healthier-looking hair.</p>
  <ul class="hero-points">
    <li>Certified 99.1% Pure GHK-Cu</li>
    <li>Independent UK Laboratory</li>
    <li>Formulated by a Board-Certified Urologist &amp; Surgeon</li>
    <li>Free Shipping Across Europe</li>
  </ul>
  <a class="btn-light">Shop All Products →</a>
  <div class="hero-visual" role="img" aria-label="Portrait of a woman holding her face, split into after and before treatment halves">
    <div class="hero-divider"></div>
    <div class="hero-tag" style="left:135px"><strong>After</strong><span>Treatment</span></div>
    <div class="hero-tag" style="left:432px"><strong>Before</strong><span>Treatment</span></div>
  </div>
</section>

<section class="section features">
  <div class="feature" style="left:125px"><h3>Tri-Peptide Science</h3><p>GHK-Cu is a naturally occurring copper peptide that activates over 70 genes involved in collagen synthesis, tissue regeneration, and skin repair, helping restore healthier, younger-looking skin.</p></div>
  <div class="feature" style="left:372px"><h3>Independent Verification</h3><p>Every Lunavel formulation is independently tested in a certified laboratory in London, UK. Each batch is verified for 99%+ purity with a Certificate of Analysis available upon request.</p></div>
  <div class="feature" style="left:618px"><h3>Surgeon-Grade Safety</h3><p>Developed by a medical doctor and manufactured to pharmaceutical standards. Safe for daily dermal use and suitable for supporting skin recovery following cosmetic and surgical procedures.</p></div>
  <div class="feature" style="left:875px"><h3>Visible Results</h3><p>Clinical research demonstrates improvements in skin firmness, elasticity, collagen production, and hair density within 8–12 weeks of consistent application.</p></div>
</section>

<section class="section gallery">
  <div class="wrap sec-head"><div class="eyebrow">REAL RESULTS</div><h2>Before &amp; After Gallery</h2><p>Real patient transformations documented over 10–16 weeks.</p></div>
  <a class="view-all">View all cases →</a>
  <div class="case" style="left:125px">
    <div class="case-photo" style="left:0;background:radial-gradient(ellipse 60% 50% at 55% 45%,#d3a485,transparent 75%),linear-gradient(135deg,#b88a6c,#8f6149)" role="img" aria-label="Woman's cheek after treatment"><span>After</span></div>
    <div class="case-photo" style="left:155px;background:radial-gradient(ellipse 60% 50% at 55% 45%,#cf9a78,transparent 75%),linear-gradient(135deg,#c0906f,#8d5c44)" role="img" aria-label="Woman's cheek before treatment"><span>Before</span></div>
    <div class="case-bar">Face Cream - 12 Weeks<small>52, Female</small></div>
  </div>
  <div class="case" style="left:445px">
    <div class="case-photo" style="left:0;background:radial-gradient(ellipse 55% 45% at 50% 55%,#dcbca6,transparent 75%),linear-gradient(180deg,#4a3a32,#c9a993 35%,#9c7a66)" role="img" aria-label="Young man's face after treatment"><span>After</span></div>
    <div class="case-photo" style="left:155px;background:radial-gradient(ellipse 55% 45% at 50% 55%,#d6ae96,transparent 75%),linear-gradient(180deg,#3e302a,#c6a08a 35%,#8f6a57)" role="img" aria-label="Young man's face before treatment"><span>Before</span></div>
    <div class="case-bar">Face Cream - 12 Weeks<small>52, Female</small></div>
  </div>
  <div class="case" style="left:765px">
    <div class="case-photo" style="left:0;background:linear-gradient(180deg,#f4f1ef,#d6b8a2 45%,#c9ac98 65%,#2a2a2a 85%)" role="img" aria-label="Man's scalp with thinning hair"><span>After</span></div>
    <div class="case-photo" style="left:155px;background:linear-gradient(180deg,#f6f4f2,#8a6448 40%,#c9a084 62%,#b9b9b9 85%)" role="img" aria-label="Man's full head of hair"><span>Before</span></div>
    <div class="case-bar">Face Cream - 12 Weeks<small>52, Female</small></div>
  </div>
</section>

<section class="section products">
  <div class="wrap sec-head"><div class="eyebrow">THE COLLECTION</div><h2>Shop the 2% GHK-Cu Range</h2><p>Doctor-formulated creams for scalp, face and body.</p></div>
  <article class="product" style="left:125px">
    <div class="product-shot" style="background:linear-gradient(180deg,#fff 0%,#f5c52b 35%,#f0b41a 70%,#2e64b5 100%)" role="img" aria-label="Head cream jar with yellow and blue label"></div>
    <div class="product-tag">2% GHK-Cu</div><h3>Head Renewal Cream</h3>
    <p>Supports healthier-looking hair with a nourished scalp environment and improved hair density.</p>
    <div class="stars">★★★★★</div><div class="price">€89</div>
  </article>
  <article class="product" style="left:445px">
    <div class="product-shot" style="background:linear-gradient(180deg,#5a2a2a 0%,#7b3a3a 20%,#d9b9b4 40%,#c58f88 75%,#3a2222 100%)" role="img" aria-label="Face cream bottle with dusty rose label"></div>
    <div class="product-tag">2% GHK-Cu</div><h3>Face Renewal Cream</h3>
    <p>Supports firmer, smoother-looking skin with improved elasticity and collagen support.</p>
    <div class="stars">★★★★★</div><div class="price">€89</div>
  </article>
  <article class="product" style="left:765px">
    <div class="product-shot" style="background:linear-gradient(180deg,#2a1a14 0%,#f7f4ef 30%,#f2ede6 75%,#3a2a1e 100%)" role="img" aria-label="Body lotion bottle with white label and red accents"></div>
    <div class="product-tag">2% GHK-Cu</div><h3>Body Renewal Lotion</h3>
    <p>Supports skin recovery and tone, including care of healed areas after surgical procedures.</p>
    <div class="stars">★★★★★</div><div class="price">€89</div>
  </article>
</section>

<section class="section doctor">
  <div class="doctor-visual" role="img" aria-label="Three smiling doctors in scrubs and a white coat with arms crossed"></div>
  <div class="doctor-copy">
    <div class="eyebrow">Medical Authority</div>
    <h2>The Only GHK-Cu Formula Personally Backed by a Medical Doctor</h2>
    <p>More than 70% of peptides sold online may be under-dosed or impure. That's why every Lunavel formulation is developed in collaboration with a pharmaceutical compounding specialist and independently laboratory tested in London, UK for 99%+ purity.<br>Created by a board-certified urologist and anti-aging physician, Lunavel combines medical science with pharmaceutical precision to support healthier skin, stronger hair, and improved tissue recovery.</p>
    <blockquote class="doctor-quote">"I only recommend products I would confidently use for myself and my own patients. Every Lunavel formulation meets the standards of purity, safety, and scientific integrity that I expect in clinical practice."</blockquote>
  </div>
</section>

<section class="section reviews">
  <div class="wrap sec-head"><div class="eyebrow">TESTIMONIALS</div><h2>What Our Customers Say</h2><p>Verified reviews from customers across Europe.</p></div>
  <article class="review" style="left:125px">
    <div class="stars">★★★★★</div>
    <p>"I've been taking Nuvora for over a year. Since starting, I haven't had a single cold or flu. My doctor was skeptical until he looked at the ingredients — now he takes it too."</p>
    <div class="reviewer"><div class="avatar" role="img" aria-label="Customer portrait"></div><div><strong>Margaret T.</strong><span>Verified Purchase</span></div></div>
  </article>
  <article class="review" style="left:449px">
    <div class="stars">★★★★★</div>
    <p>"I work in a busy hospital and my immune system takes a beating. Nuvora has become a non-negotiable part of my daily routine. The science behind it is what convinced me."</p>
    <div class="reviewer"><div class="avatar" role="img" aria-label="Customer portrait"></div><div><strong>David R.</strong><span>Verified Purchase</span></div></div>
  </article>
  <article class="review" style="left:774px">
    <div class="stars">★★★★★</div>
    <p>"My whole family uses Nuvora now. I appreciate that every ingredient is clearly listed with its actual dose — no hidden blends. That's rare in the supplement industry."</p>
    <div class="reviewer"><div class="avatar" role="img" aria-label="Customer portrait"></div><div><strong>Patricia K.</strong><span>Verified Purchase</span></div></div>
  </article>
</section>

<section class="section cta" role="img" aria-label="Laboratory vials in blue light behind the call to action">
  <h2>Start Your 12-Week Transformation</h2>
  <p>Experience clinically inspired skincare powered by 2% GHK-Cu. Doctor formulated, independently laboratory tested, and trusted for healthier skin, stronger hair, and visible rejuvenation.</p>
  <a class="btn-light">Shop the Collection →</a>
  <a class="cta-link">Read the Science →</a>
</section>

<footer class="section site-footer">
  <div class="foot-brand">LUNAVEL</div>
  <p class="foot-tag">Medical-grade 2% GHK-Cu skincare. Formulated by a surgeon. Verified by science.</p>
  <p class="foot-copy">© 2025 Lunavel. All rights reserved.</p>
  <ul class="foot-col" style="left:779px"><li>PRODUCTS</li><li>Head Cream</li><li>Face Cream</li><li>Body Lotion</li><li>Bundle</li></ul>
  <ul class="foot-col" style="left:895px"><li>SCIENCE</li><li>GHK-Cu Research</li><li>Clinical Studies</li><li>Lab Certificate</li><li>Journal</li></ul>
  <ul class="foot-col" style="left:1039px"><li>COMPANY</li><li>About Dr. [Name]</li><li>Contact</li><li>Shipping &amp; Returns</li><li>Privacy Policy</li></ul>
</footer>

</body>
</html>
```